Australian Civil Construction, Quarry & Mining Services needs a business card

We need a business card designed for our Civil Construction, Quarry & Mining Services based in the country in Australia.
Our Company Brackley Earthworks provide innovate solutions for infrastructure, agricultural and mining (aggregate, sand, roadbase) industry.
We would like our business cards to be double sided
Front of card: black background or something that resembles our business colours. (it doesn't have to be black we are open to options)
- Company name - Brackley Earthworks
- Either our logo or some sort of icon/picture that resembles our business
- Website - https://brackleyearthworks.com.au/
- We will have a number of different names, positions descriptions, phone numbers and emails on separate cards for each of our managers/directors

```html
<!DOCTYPE html>
<html lang="en">
<head>
<meta charset="utf-8">
<title>Brackley Earthworks – Business Card</title>
<link href="https://fonts.googleapis.com/css2?family=Archivo:wght@600;700;800&display=swap" rel="stylesheet">
<style>
  :root {
    --canvas: #efeff3;
    --card: #ffffff;
    --orange: #f08223;
    --charcoal: #3d3d3d;
    --ink: #3a3434;
  }
  html, body {
    margin: 0;
    padding: 0;
    width: 1200px;
    height: 1200px;
    overflow: hidden;
    background: var(--canvas);
    font-family: "Archivo", Arial, sans-serif;
  }
  .canvas {
    position: relative;
    width: 1200px;
    height: 1200px;
  }
  .card {
    position: absolute;
    left: 250px;
    width: 700px;
    height: 400px;
    background: var(--card);
    overflow: hidden;
  }
  .card--front { top: 160px; }
  .card--back { top: 640px; }
  .card__shapes {
    position: absolute;
    inset: 0;
    width: 700px;
    height: 400px;
  }
  .shape-orange { fill: var(--orange); }
  .shape-charcoal { fill: var(--charcoal); }

  .brand {
    position: absolute;
    left: 405px;
    top: 107px;
    width: 200px;
    text-align: center;
  }
  .brand__mark {
    display: block;
    width: 146px;
    height: 146px;
    margin: 0 auto;
    border-radius: 50%;
    background: var(--charcoal);
  }
  .brand__name {
    margin-top: 16px;
    font-size: 19px;
    font-weight: 700;
    color: var(--ink);
    white-space: nowrap;
    letter-spacing: 0.2px;
  }

  .person {
    position: absolute;
    left: 60px;
    top: 100px;
  }
  .person__name {
    font-size: 23px;
    font-weight: 700;
    color: var(--ink);
    line-height: 1;
  }
  .person__role {
    margin-top: 6px;
    font-size: 10.5px;
    font-weight: 700;
    color: var(--orange);
    letter-spacing: 1.6px;
  }
  .contacts {
    position: absolute;
    left: 56px;
    top: 170px;
    margin: 0;
    padding: 0;
    list-style: none;
  }
  .contacts__item {
    display: flex;
    align-items: flex-start;
    gap: 8px;
    margin-bottom: 9px;
    font-size: 14.5px;
    font-weight: 700;
    color: var(--ink);
    line-height: 18px;
  }
  .contacts__icon {
    flex: none;
    width: 20px;
    height: 20px;
  }
  .contacts__icon circle { fill: var(--orange); }
  .contacts__icon .glyph { fill: var(--ink); }
</style>
</head>
<body>
<main class="canvas">

  <section class="card card--front" aria-label="Card front">
    <svg class="card__shapes" viewBox="0 0 700 400" aria-hidden="true">
      <path class="shape-orange" d="M0 0 H60 Q88 0 102 24 L347 400 H0 Z"/>
      <path class="shape-charcoal" d="M0 0 L204 338 H0 Z"/>
    </svg>
    <div class="brand">
      <span class="brand__mark"></span>
      <div class="brand__name">BRACKLEY EARTHWORKS</div>
    </div>
  </section>

  <section class="card card--back" aria-label="Card back">
    <svg class="card__shapes" viewBox="0 0 700 400" aria-hidden="true">
      <path class="shape-orange" d="M700 0 H640 Q612 0 598 24 L353 400 H700 Z"/>
      <path class="shape-charcoal" d="M700 0 L496 338 H700 Z"/>
    </svg>

    <div class="person">
      <div class="person__name">THOMAS REID</div>
      <div class="person__role">CHIEF EXECUTIVE OFFICER</div>
    </div>

    <ul class="contacts">
      <li class="contacts__item">
        <svg class="contacts__icon" viewBox="0 0 20 20" aria-hidden="true">
          <circle cx="10" cy="10" r="10"/>
          <path class="glyph" d="M6.5 5 L8.5 5 L9.2 7.6 L8 8.6 Q9 10.8 11.4 12 L12.4 10.8 L15 11.5 L15 13.5 Q14.5 14.8 13 14.8 Q5.2 14 5.2 6.5 Q5.3 5.2 6.5 5 Z"/>
        </svg>
        <span>03 5000 1234</span>
      </li>
      <li class="contacts__item">
        <svg class="contacts__icon" viewBox="0 0 20 20" aria-hidden="true">
          <circle cx="10" cy="10" r="10"/>
          <path class="glyph" d="M10 4 A4 4 0 0 1 14 8 Q14 10.5 10 15.5 Q6 10.5 6 8 A4 4 0 0 1 10 4 Z M10 6.4 A1.6 1.6 0 1 0 10 9.6 A1.6 1.6 0 1 0 10 6.4 Z" fill-rule="evenodd"/>
        </svg>
        <span>14 Ridgeline Road, Tarrawin<br>Victoria 3999, Australia</span>
      </li>
      <li class="contacts__item">
        <svg class="contacts__icon" viewBox="0 0 20 20" aria-hidden="true">
          <circle cx="10" cy="10" r="10"/>
          <path class="glyph" d="M5 6.5 H15 V13.5 H5 Z"/>
          <path d="M5.3 6.8 L10 10.5 L14.7 6.8" fill="none" stroke="#f08223" stroke-width="1.2"/>
        </svg>
        <span>admin@brackleyearthworks.com.au</span>
      </li>
      <li class="contacts__item">
        <svg class="contacts__icon" viewBox="0 0 20 20" aria-hidden="true">
          <circle cx="10" cy="10" r="10"/>
          <circle class="glyph" cx="10" cy="10" r="5" style="fill: var(--ink)"/>
          <path d="M5 10 H15 M10 5 Q7 10 10 15 M10 5 Q13 10 10 15" fill="none" stroke="#f08223" stroke-width="0.9"/>
        </svg>
        <span>https://brackleyearthworks.com.au/</span>
      </li>
    </ul>
  </section>

</main>
</body>
</html>
```